Business cards and stationary for a fabrication company
Harborline Works
Business cards and stationary for a fabrication company - Manufacturing
Creative Brief
Modern
Dale Monroy
CEO
Generic
Dmonroy@harborline-works.com
www.Harborline-Works.com

```html
<!DOCTYPE html>
<html lang="en">
<head>
<meta charset="utf-8">
<title>Harborline Works – Business Card</title>
<link rel="stylesheet" href="https://fonts.googleapis.com/css2?family=Teko:wght@500;600&family=Oswald:wght@500&display=swap">
<style>
  :root {
    --backdrop: #3b3b3b;
    --card: #ffffff;
    --red: #e8261c;
    --blue: #2b39b8;
    --ink: #1c1c1c;
    --white: #ffffff;
  }
  html, body {
    margin: 0;
    padding: 0;
    width: 1200px;
    height: 694px;
    overflow: hidden;
    background: var(--backdrop);
  }
  .card {
    position: absolute;
    left: 233px;
    top: 113px;
    width: 734px;
    height: 473px;
    background: var(--card);
    overflow: hidden;
  }
  .card-shapes {
    position: absolute;
    inset: 0;
  }
  .brand {
    position: absolute;
    left: 215px;
    top: 40px;
    display: flex;
    align-items: center;
    gap: 18px;
  }
  .brand-mark {
    width: 70px;
    height: 70px;
    border-radius: 50%;
    background: var(--red);
  }
  .brand-name {
    font-family: "Teko", sans-serif;
    font-weight: 600;
    font-size: 66px;
    line-height: 1;
    color: var(--red);
    letter-spacing: 1px;
    padding-top: 8px;
  }
  .person {
    position: absolute;
    left: 120px;
    right: 0;
    top: 232px;
    text-align: center;
    color: var(--white);
    font-family: "Teko", sans-serif;
  }
  .person-name {
    font-weight: 600;
    font-size: 58px;
    line-height: 46px;
    letter-spacing: 1px;
    margin: 0;
  }
  .person-role {
    font-weight: 500;
    font-size: 24px;
    line-height: 20px;
    margin: 0;
  }
  .contact {
    position: absolute;
    left: 80px;
    top: 306px;
    margin: 0;
    padding: 0;
    list-style: none;
    font-family: "Oswald", sans-serif;
    font-weight: 500;
    font-size: 16px;
    color: var(--ink);
  }
  .contact-item {
    display: flex;
    align-items: center;
    gap: 20px;
    height: 38px;
  }
  .contact-icon {
    width: 16px;
    height: 16px;
    flex: none;
  }
</style>
</head>
<body>
  <div class="card">
    <svg class="card-shapes" width="734" height="473" viewBox="0 0 734 473">
      <rect class="corner-tab" x="-30" y="-30" width="105" height="105" rx="24" fill="var(--red)"/>
      <polygon class="diagonal-band" points="0,92 132,224 132,302 118,302 0,184" fill="var(--blue)"/>
      <polygon class="diagonal-stripe" points="0,200 102,302 62,302 0,240" fill="var(--red)"/>
      <path class="name-band" d="M150 222 H734 V302 H118 V254 Q118 222 150 222 Z" fill="var(--blue)"/>
      <path class="corner-sweep" d="M380 473 Q430 372 734 360 V473 Z" fill="var(--red)"/>
    </svg>

    <div class="brand">
      <span class="brand-mark"></span>
      <span class="brand-name">HARBORLINE WORKS</span>
    </div>

    <div class="person">
      <p class="person-name">DALE MONROY</p>
      <p class="person-role">CEO</p>
    </div>

    <ul class="contact">
      <li class="contact-item">
        <svg class="contact-icon" viewBox="0 0 16 16"><path d="M4 1.5 6.5 4.5 5 6.5Q6.5 9.5 9.5 11L11.5 9.5 14.5 12 12.5 14.5Q7 14 3.5 10T1.5 3.5Z" fill="var(--blue)"/></svg>
        <span>903-555-0142</span>
      </li>
      <li class="contact-item">
        <svg class="contact-icon" viewBox="0 0 16 16" fill="none" stroke="var(--blue)" stroke-width="1.4"><circle cx="8" cy="8" r="6.5"/><ellipse cx="8" cy="8" rx="2.8" ry="6.5"/><path d="M1.5 8H14.5M2.5 4.8H13.5M2.5 11.2H13.5"/></svg>
        <span>WWW.HARBORLINE-WORKS.COM</span>
      </li>
      <li class="contact-item">
        <svg class="contact-icon" viewBox="0 0 16 16" fill="none" stroke="var(--blue)" stroke-width="1.4"><rect x="1.5" y="3.5" width="13" height="9"/><path d="M1.5 3.5 8 9 14.5 3.5"/></svg>
        <span>DMONROY@HARBORLINE-WORKS.COM</span>
      </li>
    </ul>
  </div>
</body>
</html>
```